Fashion Wholesale Product Page

We need a product page layout for a wholesale catalogue.
It will include a title, 3 images, short description, prices and size and colour options in an a5 page for print.
We'd like a design file that we can use to update with new products in the future.
All images and content will be provided.
The range we are selling is all about simplicity and minimalism so we'd love this to be reflected in the layout.

Target Market(s)

Young, fashion conscious women with a strong appreciation for good, simple design.

Industry/Entity Type

Fashion

Requirements
Must have
• Title - 'Triangle Bra'
Short Description - 'Perfect for a smaller bust, the triangle bra is divine simplicity. Featuring our well known triangle cut and darted cups, we have perfected this design for an optimal fit.'
Prices - Wholesale: $30 RRP: $60
Available in -
Colours Black, White, Grey Marle
Sizes XS, S, M, L

3 product images
Nice to have
• If it fits with the design it would be great to include the image on the model attached here.

I don't want it to feel too crowded though.

```html
<!DOCTYPE html>
<html lang="en">
<head>
<meta charset="utf-8">
<title>Triangle Bra – Wholesale Product Page</title>
<link rel="stylesheet" href="https://fonts.googleapis.com/css2?family=Stint+Ultra+Condensed&family=Fira+Sans+Condensed:wght@400&family=Cabin:wght@400&display=swap">
<style>
  :root {
    --panel-black: #000000;
    --paper-white: #ffffff;
    --text-white: #ffffff;
    --text-grey: #c9c9c9;
    --product-black: #1c1c1c;
    --product-white: #eeeeef;
    --product-grey: #b4b4b4;
  }
  * { margin: 0; padding: 0; box-sizing: border-box; }
  html, body {
    width: 1200px;
    height: 900px;
    overflow: hidden;
    background: var(--paper-white);
  }
  .product-page {
    position: relative;
    width: 1200px;
    height: 900px;
    display: flex;
  }
  .info-panel {
    width: 775px;
    height: 900px;
    background: var(--panel-black);
    position: relative;
  }
  .product-title {
    position: absolute;
    left: 0;
    width: 756px;
    top: 92px;
    text-align: center;
    font-family: "Stint Ultra Condensed", serif;
    font-weight: 400;
    font-size: 118px;
    line-height: 1;
    color: var(--text-white);
    letter-spacing: 1px;
  }
  .product-description {
    position: absolute;
    left: 131px;
    width: 506px;
    top: 288px;
    font-family: "Fira Sans Condensed", sans-serif;
    font-size: 25px;
    line-height: 47px;
    text-align: justify;
    color: var(--text-white);
  }
  .product-details {
    position: absolute;
    left: 170px;
    width: 400px;
    top: 558px;
    text-align: center;
    font-family: "Cabin", sans-serif;
    font-size: 25px;
    line-height: 42px;
    color: var(--text-grey);
  }
  .price-list { margin-bottom: 42px; }
  .gallery-panel {
    flex: 1;
    height: 900px;
    background: var(--paper-white);
    position: relative;
  }
  .product-shot {
    position: absolute;
    display: block;
  }
  .shot-black { left: 60px; top: 35px; }
  .shot-white { left: 65px; top: 308px; }
  .shot-grey  { left: 65px; top: 600px; }
</style>
</head>
<body>
<main class="product-page">
  <section class="info-panel">
    <h1 class="product-title">Triangle Bra</h1>
    <p class="product-description">Perfect for a smaller bust, the triangle bra is divine simplicity. Featuring our well known triangle cut and darted cups, we have perfected this design for optimal fit.</p>
    <div class="product-details">
      <div class="price-list">
        <p class="price-wholesale">Wholesale : $30</p>
        <p class="price-retail">RRP : $60</p>
      </div>
      <div class="options-list">
        <p>Available in -</p>
        <p class="colour-options">Black, White, Grey Marle</p>
        <p class="size-options">Sizes XS,S,M,L</p>
      </div>
    </div>
  </section>
  <section class="gallery-panel">
    <svg class="product-shot shot-black" width="320" height="245" role="img" aria-label="Product photo: triangle bra in black, laid flat">
      <rect width="320" height="245" fill="var(--product-black)"/>
    </svg>
    <svg class="product-shot shot-white" width="325" height="268" role="img" aria-label="Product photo: triangle bra in white, laid flat">
      <rect width="325" height="268" fill="var(--product-white)"/>
    </svg>
    <svg class="product-shot shot-grey" width="322" height="290" role="img" aria-label="Product photo: triangle bra in grey marle with black trim, laid flat">
      <rect width="322" height="290" fill="var(--product-grey)"/>
    </svg>
  </section>
</main>
</body>
</html>
```